Over 100 ladies will be traveling to Ocean City, MD for a Women's Retreat Conference. This flyer is for advertisement. This flyer is to circulate for registrations as well as to post on social media. Theme is Holy Spirit fire. I have attached a photo. All the information in the attachment should be included on the flyer. Information should be clearly readable end eye catching.

Target Market(s)

Church ladies

Industry/Entity Type

Religious

Font styles to use
Sans Serif

Colors

Designer to choose colors to be used in the design.

Requirements
Must have
• Title: Brightvale Womens Gathering 2019 "FIRE"
• All components in attachments

```html
<!DOCTYPE html>
<html lang="en">
<head>
<meta charset="utf-8">
<title>Brightvale Womens Gathering 2019 "FIRE" Conference</title>
<link rel="stylesheet" href="https://fonts.googleapis.com/css2?family=Alfa+Slab+One&family=Bebas+Neue&family=Roboto:wght@300;400;500;700;900&display=swap">
<style>
:root{
  --ink:#0c0505;
  --ember:#3a0606;
  --flame-red:#c8160c;
  --flame-orange:#f26a10;
  --flame-yellow:#ffd21a;
  --gold:#ffd400;
  --gold-soft:#f4e0a8;
  --cream:#fffbe8;
  --white:#ffffff;
}
*{margin:0;padding:0;box-sizing:border-box}
html,body{width:927px;height:1200px;overflow:hidden;background:var(--ink)}
.flyer{position:relative;width:927px;height:1200px;overflow:hidden;font-family:"Roboto",sans-serif;color:var(--white);
  background:radial-gradient(ellipse 46% 60% at 50% 52%, #1a0606 0%, #2a0707 45%, var(--ember) 70%, #7a0d08 100%);}
.flames{position:absolute;inset:0;
  background:
   linear-gradient(90deg, rgba(255,180,20,.95) 0%, rgba(242,106,16,.85) 7%, rgba(200,22,12,.75) 15%, rgba(120,10,6,0) 24%),
   linear-gradient(270deg, rgba(255,180,20,.95) 0%, rgba(242,106,16,.85) 7%, rgba(200,22,12,.75) 15%, rgba(120,10,6,0) 24%),
   linear-gradient(180deg, rgba(200,22,12,.55) 0%, rgba(0,0,0,0) 20%, rgba(0,0,0,0) 75%, rgba(140,14,8,.6) 100%);}
.header-band{position:absolute;left:0;top:84px;width:927px;height:112px;background:linear-gradient(180deg,#1a1412,#0d0a09);
  border-top:2px solid rgba(255,210,120,.6);border-bottom:2px solid rgba(255,210,120,.6);display:flex;align-items:center;justify-content:center}
.event-title{font-family:"Bebas Neue",sans-serif;font-size:70px;letter-spacing:1px;line-height:1;
  background:linear-gradient(180deg,#fff8e0 0%,#f3dca0 55%,#c99a45 100%);-webkit-background-clip:text;background-clip:text;color:transparent}
.theme{position:absolute;left:0;top:222px;width:927px;text-align:center;font-family:"Alfa Slab One",serif;font-size:132px;line-height:1;
  background:linear-gradient(180deg,#ffffff 0%,#fff4d6 45%,#d9a64a 100%);-webkit-background-clip:text;background-clip:text;color:transparent;
  filter:drop-shadow(0 0 1px #b4620e) drop-shadow(3px 4px 0 #3b1a06)}
.subtitle{position:absolute;left:0;top:380px;width:927px;text-align:center;font-weight:300;font-size:33px;letter-spacing:8px;padding-left:8px}
.portrait{position:absolute;top:454px;width:118px;height:172px;border:4px solid var(--gold);
  background:linear-gradient(180deg,#e9dccb 0%,#b08a70 55%,#3a2a26 100%)}
.role{position:absolute;top:634px;font-weight:900;font-size:17px;color:var(--gold);text-align:center;white-space:nowrap}
.person{position:absolute;top:660px;text-align:center;white-space:nowrap}
.person .name{font-weight:700;font-size:11.5px;display:block}
.person .place{font-weight:500;font-size:9.5px;display:block;margin-top:2px}
.venue-photo{position:absolute;width:156px;height:156px;border-radius:50%;border:4px solid var(--gold)}
.included{position:absolute;left:498px;top:722px;width:270px}
.included h2{font-weight:500;font-size:20px;color:var(--gold);margin-bottom:6px}
.included li{list-style:none;font-size:17px;line-height:30px;border-bottom:1px solid rgba(255,212,0,.55)}
.included li:last-child{border-bottom:none}
.cost{position:absolute;left:494px;top:880px;width:282px;height:66px;background:var(--gold);border-radius:6px;color:#111;padding:6px 0 0 22px}
.cost .price{font-weight:500;font-size:34px;line-height:1.05;display:block}
.cost .note{font-weight:500;font-size:10.5px;display:block}
.venue{position:absolute;left:498px;top:958px;font-size:16px;line-height:20px}
.venue strong{font-weight:700;font-size:19.5px;display:block;line-height:24px}
.terms{position:absolute;left:0;top:1045px;width:927px;text-align:center;font-size:13.4px;line-height:18px}
.contact{position:absolute;left:0;top:1101px;width:927px;text-align:center;font-size:20px;line-height:26px}
</style>
</head>
<body>
<main class="flyer">
  <div class="flames" role="img" aria-label="Bright flames rising along both sides of the flyer"></div>

  <header class="header-band"><h1 class="event-title">BRIGHTVALE WOMENS GATHERING 2019</h1></header>
  <div class="theme">"FIRE"</div>
  <div class="subtitle">CONFERENCE</div>

  <div class="portrait" style="left:240px" role="img" aria-label="Portrait of retreat host Apostle Dena Whitfield"></div>
  <div class="portrait" style="left:420px" role="img" aria-label="Portrait of speaker Pastor Lorna Greene"></div>
  <div class="portrait" style="left:588px" role="img" aria-label="Portrait of speaker Pastor Celia Marsh"></div>

  <div class="role" style="left:201px;width:200px">RETREAT HOST</div>
  <div class="role" style="left:440px;width:240px">RETREAT SPEAKERS</div>
  <div class="person" style="left:201px;width:200px"><span class="name">APOSTLE DENA WHITFIELD</span></div>
  <div class="person" style="left:401px;width:160px"><span class="name">PASTOR LORNA GREENE</span><span class="place">ORLANDO, FLORIDA</span></div>
  <div class="person" style="left:568px;width:160px"><span class="name">PASTOR CELIA MARSH</span><span class="place">HLCM - WALDORF, MD.</span></div>

  <div class="venue-photo" style="left:134px;top:706px;background:linear-gradient(180deg,#7fb6d8 0%,#3d7ea8 45%,#e9e2cf 80%,#f3efe4 100%)" role="img" aria-label="Aerial view of the beachfront hotel"></div>
  <div class="venue-photo" style="left:302px;top:706px;background:linear-gradient(180deg,#9fb8d6 0%,#b89a88 40%,#6b5044 100%)" role="img" aria-label="Hotel facade with twin towers"></div>
  <div class="venue-photo" style="left:134px;top:870px;background:linear-gradient(180deg,#c8d8dc 0%,#9fbcc4 45%,#f2f2ee 80%,#b8c4c4 100%)" role="img" aria-label="Guest room with two beds"></div>
  <div class="venue-photo" style="left:302px;top:870px;background:linear-gradient(180deg,#f4eee2 0%,#e2d8c4 50%,#a8a39a 100%)" role="img" aria-label="Grand lobby with chandelier and staircase"></div>

  <section class="included">
    <h2>INCLUDED:</h2>
    <ul>
      <li>All Retreat Sessions</li>
      <li>2 Nights Hotel Accommodations</li>
      <li>1 Hot Lunch Buffet</li>
      <li>1 Full Hot American Breakfast</li>
    </ul>
  </section>

  <div class="cost"><span class="price">COST:&nbsp; $295</span><span class="note">*BASED ON DOUBLE OCCUPANCY</span></div>

  <address class="venue" style="font-style:normal"><strong>SEABREEZE HARBOR HOTEL &amp; SUITES</strong>1450 HARBOR VIEW AVE.<br>OCEAN CITY, MARYLAND 21842</address>

  <p class="terms">**ALL deposits/registrations are NON-refundable and NON-transferable. Your entire registration is due<br>by October 1, 2018. Please submit your desired roommate's name at the time of registration.<br>If you do not choose a roommate one will be assigned to you unless you have registered for a private room.</p>
  <p class="contact">Please contact Marla via email marla@whitfieldministries.com or<br>phone 240-555-0148 for more information.</p>
</main>
</body>
</html>
```